Velmorytrips.com web design project + logo design

Hi,

We are a Russian online tour operator - roamquiltex.com

We are looking to tranmsfer our domain to velmorytrips.com. The website and logo need to be velmoryesque - we are not looking to change our functionality, but we need to make the website much more attracitve to clients, much more wild looking but at the same time remaining a professional travel company.

The main concept of the website should be innovative travel (as velmory was an innovator). Alternatively, you could go down the artist route and go down the draw / design your own tour road.

On our website the customer is able to combine travel services (hotels, flights, Visa services, and soon chauffeur, car rental etc...) put it into their basket (the basket definitely has to look better than it is at the moment) and pay for it in one go by card.

We are also stressin our customer support with web chat, call centre etc... (call centre number at the top of the page)

We aim to provide an easy user experience, but we need to make it have some more style, so I will be waiting for what you guys can come up with.
Let me know if you have any questions - skype is: mrkostelin

Industry/Entity Type

It Company

Logo Text

Requirements
Must have
• It is quite a simple task - to take the existing website roamquiltex.com and velmorysize it to create velmorytrips.com, the functionality of the website will remain the same and there are not many pages in the website. Homepage, Checkout step1, Checkout step 2 (you can view both of these if you select a service) and the generic pages for T&C''s, Privacy policy etc...

IMPORTANT UPDATE

We are also looking at how the search results will look in the designs, (please do a search on our website for hotel / flight)

```html
<!DOCTYPE html>
<html lang="en">
<head>
<meta charset="utf-8">
<title>Velmorytrips.com</title>
<link href="https://fonts.googleapis.com/css2?family=IM+Fell+English&family=IM+Fell+English+SC&family=Arimo:wght@400;700&display=swap" rel="stylesheet">
<style>
:root{
  --parchment-light:#ecd3a0;
  --parchment:#d9a862;
  --parchment-dark:#a8692c;
  --brown-deep:#3b2410;
  --brown:#5a3714;
  --brown-mid:#7a4d1c;
  --gold:#e9c77a;
  --gold-dark:#c99a3e;
  --cream:#f4ecdd;
  --ink:#2a1a0a;
  --white:#ffffff;
  --tab:#e8d3a3;
  --serif:"IM Fell English", Georgia, serif;
  --serif-sc:"IM Fell English SC", Georgia, serif;
  --sans:"Arimo", Arial, sans-serif;
}
*{box-sizing:border-box;margin:0;padding:0}
html,body{width:1200px;height:1000px;overflow:hidden;background:var(--white)}
.canvas{position:relative;width:1200px;height:1000px;background:var(--white)}
.page{position:absolute;left:72px;top:0;width:1068px;height:1000px;
  background:radial-gradient(ellipse at 55% 45%,var(--parchment-light) 0%,var(--parchment) 55%,var(--parchment-dark) 100%);}
.abs{position:absolute}
.brand{left:230px;top:72px;width:225px;display:flex;align-items:center;gap:8px}
.brand-dot{width:20px;height:20px;border-radius:50%;background:var(--brown-deep)}
.brand-name{font-family:var(--serif);font-size:23px;color:var(--brown-deep);white-space:nowrap}
.hotline{right:530px;top:58px;text-align:right;color:var(--white);font-family:var(--serif);text-shadow:0 1px 2px var(--ink);white-space:nowrap}
.hotline .free{font-size:24px;line-height:27px}
.hotline .phone{font-size:19px;line-height:21px}
.hotline .hours{font-size:13px;line-height:17px}
.dark-box{background:linear-gradient(var(--brown-mid),var(--brown-deep));border-radius:3px;border:1px solid #2a1608}
.settings{left:678px;top:62px;width:268px;height:28px;display:flex;align-items:center;gap:6px;padding:0 8px;font-family:var(--serif);font-size:12px;color:var(--cream);white-space:nowrap}
.select{height:14px;background:#b9b2a6;border-radius:2px;font-family:var(--sans);font-size:7px;color:#eee;padding:2px 14px 0 4px;position:relative}
.select::after{content:"";position:absolute;right:0;top:0;width:11px;height:14px;background:#8a8378}
.cart{left:678px;top:93px;width:268px;height:36px;display:flex;align-items:center;padding:0 8px;gap:6px}
.globe{width:26px;height:26px;border-radius:50%;background:radial-gradient(circle at 40% 35%,#8fb0c8,#4a6b3a)}
.cart-text{font-family:var(--serif);font-size:12px;color:var(--cream);line-height:13px;flex:1}
.cart-text small{font-size:10px}
.btn-gold{background:linear-gradient(var(--gold),var(--gold-dark));border-radius:2px;font-family:var(--serif);color:var(--ink);display:flex;align-items:center;justify-content:center;gap:6px}
.checkout{width:106px;height:24px;font-size:13px}
.nav{left:455px;top:133px;width:491px;height:33px;display:flex;align-items:center;padding-left:8px}
.nav a{font-family:var(--serif);font-size:13px;color:var(--gold);text-decoration:none;width:83px;text-align:center;border-right:1px solid #8a6a3a;line-height:20px}
.nav a.active{color:var(--white)}
.nav a:nth-child(4){border-right:none}
.nav-search{margin-left:6px;width:110px;height:14px;background:var(--white)}
.nav-go{margin-left:4px;width:16px;height:16px;border-radius:50%;background:var(--gold-dark);border:2px solid var(--gold)}
.hero{left:265px;top:176px;width:680px;height:203px;border:3px solid var(--brown);border-radius:4px;overflow:hidden;
  background:linear-gradient(180deg,#c9d4dc 0%,#a8b0a8 40%,#4c5a2e 62%,#3a4420 100%)}
.hero-caption{left:3px;top:95px;width:240px;height:78px;background:rgba(60,35,12,.75);padding:14px 0 0 44px;font-family:var(--serif);font-size:20px;line-height:25px;color:var(--white)}
.hero-arrow{top:92px;width:0;height:0;border-top:10px solid transparent;border-bottom:10px solid transparent}
.hero-arrow.left{left:8px;border-right:12px solid var(--gold)}
.hero-arrow.right{right:8px;border-left:12px solid var(--gold)}
.booking{left:263px;top:385px;width:685px;height:238px;background:var(--brown);border-radius:4px}
.tabs{left:6px;top:7px;width:182px;height:178px;background:var(--tab)}
.tab{height:44.5px;display:flex;align-items:center;gap:10px;padding-left:16px;font-family:var(--serif);font-size:16px;color:var(--brown-deep);border-bottom:1px solid #cdb37f}
.tab.active{background:var(--brown-mid);color:var(--white)}
.tab-dot{width:14px;height:14px;border-radius:50%;background:var(--brown-mid);border:3px solid var(--gold-dark)}
.form{left:193px;top:9px;width:482px;height:111px;background:var(--white);border-radius:3px;font-family:var(--serif);font-size:13px;color:var(--ink)}
.form .lbl{position:absolute}
.field{position:absolute;height:20px;border:1px solid #ccc;border-radius:2px;background:var(--white)}
.mini{font-family:var(--sans);font-size:9px;color:#888}
.search-btn{left:360px;top:86px;width:106px;height:22px;font-size:13px}
.calendar{left:193px;top:123px;width:482px;height:107px;background:var(--white);border-radius:3px;overflow:hidden}
.cal-month{height:14px;font-family:var(--serif);font-size:10px;padding-left:10px;color:var(--ink);border-bottom:1px solid #ddd}
.cal-days{display:flex;height:93px}
.cal-day{flex:1;border-right:1px solid #ddd;text-align:center;font-family:var(--sans);font-size:8px;color:#26446b;padding-top:2px}
.cal-day:last-child{border-right:none}
.info-card{top:628px;width:221px;height:199px;background:rgba(90,55,20,.5);border-radius:4px;padding:4px}
.card-head{height:28px;background:linear-gradient(var(--brown-mid),var(--brown));display:flex;align-items:center;gap:8px;padding-left:4px;font-family:var(--serif);font-size:16px;color:var(--white)}
.card-icon{width:30px;height:30px;margin-top:-4px;background:var(--tab);border:2px solid var(--gold-dark)}
.card-body{margin-top:4px;height:159px;background:var(--cream);border-radius:3px;padding:6px;font-family:var(--sans);font-size:9.2px;line-height:11px;color:#333;position:relative}
.card-title{font-family:var(--serif);font-size:13px;color:var(--ink);margin-bottom:8px;white-space:nowrap}
.card-sub{font-family:var(--serif);font-size:12px;color:#6b2e0a;text-align:center;margin-bottom:6px;font-weight:bold}
.tick-row{display:flex;gap:4px;margin-bottom:8px;text-align:justify}
.tick{flex:0 0 12px;height:12px}
.more{position:absolute;right:12px;bottom:4px;font-size:10px}
.foot-h{font-family:var(--serif);font-size:17px;color:var(--ink)}
.foot-list{list-style:none;font-family:var(--sans);font-size:9px;color:var(--ink);line-height:20px}
.foot-addr{font-family:var(--sans);font-size:9px;font-weight:bold;color:var(--ink);line-height:11px}
.social{width:24px;height:24px;background:#8a7a5a;border:1px solid #5a4a30;border-radius:2px}
.contact-row{display:flex;align-items:center;gap:8px;font-family:var(--serif);font-size:16px;color:var(--ink);white-space:nowrap}
.contact-icon{width:20px;height:20px;border-radius:3px;background:var(--brown-mid);border:1px solid var(--brown-deep)}
.rss{width:20px;height:20px;border-radius:3px;background:#d26a1c}
.subscribe{display:flex;gap:6px;align-items:center}
.sub-field{width:112px;height:22px;background:var(--white);border:1px solid #bbb}
.send{width:40px;height:22px;font-size:13px}
.legal{font-family:var(--sans);font-size:7.5px;color:var(--ink)}
.chat{left:826px;top:868px;width:118px;height:126px;border:5px solid #9c7a2c;background:linear-gradient(160deg,#5a3a18,#2a1a0a)}
.chat-label{left:0;bottom:0;width:100%;text-align:center;font-family:var(--serif);font-size:14px;color:var(--gold)}
</style>
</head>
<body>
<div class="canvas">
  <div class="page" role="img" aria-label="Aged parchment background with faint inventor sketches of flying machines, gears and a bearded portrait"></div>

  <header>
    <div class="abs brand"><span class="brand-dot"></span><span class="brand-name">Velmorytrips.com</span></div>
    <div class="abs hotline">
      <div class="free">8-800-555-0142</div>
      <div class="phone">Phone: +7 (495) 555 01 27</div>
      <div class="hours">(Mon - Fri) hours: 9:00 am - 6:00 pm</div>
    </div>
    <div class="abs dark-box settings">
      <span>Language:</span><span class="select">English</span>
      <span style="margin-left:16px">Currency</span><span class="select">US Dollar</span>
    </div>
    <div class="abs dark-box cart">
      <span class="globe"></span>
      <span class="cart-text">Shopping Cart<br><small>*Pricing</small></span>
      <span class="btn-gold checkout">Check out
        <svg width="14" height="14" viewBox="0 0 14 14"><path d="M2 7l4 4 7-10" stroke="#2a1a0a" stroke-width="2.4" fill="none"/></svg></span>
    </div>
    <nav class="abs dark-box nav">
      <a href="#" class="active">Home</a><a href="#">Forum</a><a href="#">My Tour</a><a href="#">Contact</a>
      <span class="nav-search"></span><span class="nav-go"></span>
    </nav>
  </header>

  <section class="abs hero" role="img" aria-label="Photo of a stepped Mayan stone pyramid rising above jungle trees under a cloudy sky">
    <div class="abs hero-caption">Incredible Offer<br>Trip to Guatemala</div>
    <span class="abs hero-arrow left"></span><span class="abs hero-arrow right"></span>
  </section>

  <section class="abs booking">
    <div class="abs tabs">
      <div class="tab active"><span class="tab-dot"></span>Tickets</div>
      <div class="tab"><span class="tab-dot"></span>Information</div>
      <div class="tab"><span class="tab-dot"></span>Hotels</div>
      <div class="tab"><span class="tab-dot"></span>Packages</div>
    </div>
    <form class="abs form">
      <span class="lbl" style="left:11px;top:8px">When</span>
      <span class="field" style="left:82px;top:6px;width:144px"></span>
      <span class="lbl" style="left:233px;top:8px">Where</span>
      <span class="field" style="left:272px;top:6px;width:144px"></span>
      <span class="lbl" style="left:11px;top:35px">Date</span>
      <span class="field mini" style="left:82px;top:32px;width:84px;padding:4px 0 0 24px">14-06-2013</span>
      <span class="lbl" style="left:236px;top:35px">Back</span>
      <span class="field" style="left:274px;top:32px;width:82px;background:#999"></span>
      <span class="lbl mini" style="left:362px;top:31px;font-size:8px;color:#333">&#9633; Back<br>&#9745; One way</span>
      <span class="lbl" style="left:11px;top:61px">Passengers</span>
      <span class="field mini" style="left:94px;top:60px;width:36px;height:16px;padding:2px 4px">1</span>
      <span class="field mini" style="left:170px;top:60px;width:36px;height:16px;padding:2px 4px">0</span>
      <span class="field mini" style="left:246px;top:60px;width:36px;height:16px;padding:2px 4px">0</span>
      <span class="lbl" style="left:11px;top:89px">Classs</span>
      <span class="field mini" style="left:82px;top:86px;width:80px;height:18px;padding:3px 4px">Economy</span>
      <span class="abs btn-gold search-btn">Search</span>
    </form>
    <div class="abs calendar">
      <div class="cal-month">January</div>
      <div class="cal-days">
        <div class="cal-day">Thu, 01</div><div class="cal-day">Fri, 02</div><div class="cal-day">Sat, 03</div>
        <div class="cal-day">Sun, 04</div><div class="cal-day">Mon, 05</div><div class="cal-day">Tue, 06</div><div class="cal-day">Wed, 07</div>
      </div>
    </div>
  </section>

  <section class="abs info-card" style="left:266px">
    <div class="card-head"><span class="card-icon"></span>Info</div>
    <div class="card-body">
      <div class="card-title">There are two options apply for a visa</div>
      <div class="card-sub">1.Oformlenie visa "Online"</div>
      <div class="tick-row"><svg class="tick" viewBox="0 0 12 12"><rect x=".5" y="2" width="9" height="9" fill="none" stroke="#222"/><path d="M2 6l3 3 6-8" stroke="#222" stroke-width="2" fill="none"/></svg><span>Cmozhete you apply for a visa, send and receive back their documents "from the comfort of home!"</span></div>
      <div class="tick-row"><svg class="tick" viewBox="0 0 12 12"><rect x=".5" y="2" width="9" height="9" fill="none" stroke="#222"/><path d="M2 6l3 3 6-8" stroke="#222" stroke-width="2" fill="none"/></svg><span>After booking, the selected service, you need to fill out a simple form on the visa application form on the newly created for your personal page.</span></div>
      <span class="more">more...</span>
    </div>
  </section>
  <section class="abs info-card" style="left:495px">
    <div class="card-head"><span class="card-icon"></span>Tickets</div>
    <div class="card-body">
      <div class="card-title">Flights from Tours designer.</div>
      <p>On our site you can consider offers from different airlines and purchase tickets according to your wishes and budget.<br>Plan dates of departures and arrivals c in any country, filling the cells you want, Tour Designer automatically displays your program in the calendar.<br>On Tour Designer You can create any tour, including round-the-world and pay for all the services a single payment.</p>
    </div>
  </section>
  <section class="abs info-card" style="left:723px">
    <div class="card-head"><span class="card-icon" style="border-radius:50%"></span>Hotels</div>
    <div class="card-body">
      <div class="card-title">Hotels by City Builder.</div>
      <p>Our site offers a wide selection of hotels located in different countries and continents of the world. You can choose and book all kinds of accommodation options, according to your wishes and budget.<br>pursue their dreams!<br>We have created for you the most convenient framework for planning a vacation or business trip. Tour Builder saves your time now to buy a package tour you can just 3 simple steps:</p>
      <span class="more">more...</span>
    </div>
  </section>

  <footer>
    <div class="abs" style="left:276px;top:852px">
      <div class="foot-h">View Site</div>
      <ul class="foot-list"><li>Home</li><li>About Us</li><li>Forum</li><li>Contacts</li></ul>
    </div>
    <div class="abs" style="left:362px;top:852px">
      <div class="foot-h">Help</div>
      <ul class="foot-list"><li>Help</li><li>Terms of use</li><li>Privacy policy</li><li>Cookies</li></ul>
    </div>
    <div class="abs" style="left:437px;top:852px">
      <div class="foot-h">Find Us</div>
      <div class="foot-addr" style="margin:6px 0 0 14px">Roamquilt Limited<br>18 Harlow Lane<br>London, E2 4QT<br>UK</div>
      <div class="foot-h" style="margin-top:8px">We are in</div>
      <div style="display:flex;gap:4px;margin:4px 0 0 24px"><span class="social"></span><span class="social"></span><span class="social"></span></div>
    </div>
    <div class="abs" style="left:585px;top:868px;display:flex;flex-direction:column;gap:9px">
      <div class="contact-row"><span class="contact-icon"></span>+7 (495) 555 01 27</div>
      <div class="contact-row"><span class="contact-icon"></span>info@roamquiltex.com</div>
      <div class="contact-row"><span class="rss"></span>Exclusive Offers</div>
      <div class="subscribe" style="margin:-4px 0 0 28px"><span class="sub-field"></span><span class="btn-gold send">send</span></div>
      <div class="legal" style="margin:-8px 0 0 28px">Your data is safe, read our Privacy Policy</div>
    </div>
    <div class="abs chat" role="img" aria-label="Framed Renaissance-style portrait of a support agent wearing a headset">
      <div class="abs chat-label">Chat online</div>
    </div>
  </footer>
</div>
</body>
</html>
```